Briar Ridge Target Range wordpress theme

I want a Wordpress theme that is classy, unusual, colorful, etc. based on my attached logo files.

Font:
- Serpentine-Bold-Bold for "BRIAR RIDGE"
- BrowalliaUPC for "TARGET RANGE"

Colors (CMYK code):
- BLACK ....... 0; 0; 0; 100;
- ORANGE ... gradient from 0; 65; 97.5; 0 to 0; 39; 97.5; 0

```html
<!DOCTYPE html>
<html lang="en">
<head>
<meta charset="utf-8">
<title>Briar Ridge Target Range</title>
<link href="https://fonts.googleapis.com/css2?family=Open+Sans:ital,wght@0,400;0,600;1,400&family=Russo+One&display=swap" rel="stylesheet">
<style>
:root{
  --orange-dark:#e8651a;
  --orange-light:#f29a1e;
  --orange-text:#ee7419;
  --ink:#2b2b2b;
  --body-text:#555;
  --panel:#2b2b2b;
  --footer:#3a3a3a;
  --rule:#d6d6d6;
  --white:#fff;
}
*{margin:0;padding:0;box-sizing:border-box}
html,body{width:1029px;height:1200px;overflow:hidden;background:var(--footer)}
.page{position:relative;width:1200px;height:1400px;transform:scale(0.8575);transform-origin:0 0;background:#fff;font-family:"Open Sans",sans-serif;color:var(--body-text)}
.abs{position:absolute}
.heading{font-family:"Russo One",sans-serif;font-weight:400;color:var(--ink);letter-spacing:1px}
.heading span{color:var(--orange-text)}
.top-band{left:0;top:0;width:1200px;height:125px;background:linear-gradient(#fff,#ececec)}
.dark-band{left:0;top:125px;width:1200px;height:370px;background:linear-gradient(#4a4848,#000)}
.brand{left:130px;top:18px;width:125px;height:125px;display:flex;flex-direction:column;align-items:center;justify-content:center;gap:6px;font-family:"Open Sans",sans-serif;font-weight:600;color:var(--orange-text);font-size:15px;text-align:center;line-height:1.1}
.brand .mark{width:34px;height:34px;background:var(--orange-text)}
.call{left:850px;top:26px}
.call .label{font-family:"Russo One",sans-serif;color:var(--orange-text);font-size:16px;letter-spacing:1px}
.call .phone{font-family:"Russo One",sans-serif;color:#333;font-size:25px;letter-spacing:2px;margin-top:2px}
.nav{left:290px;top:100px;width:780px;height:45px;background:linear-gradient(var(--orange-light),var(--orange-dark));display:flex;align-items:center;list-style:none;border-radius:0 2px 2px 0}
.nav li{color:#fff;font-size:13px;letter-spacing:.6px;padding:0 21px;height:45px;line-height:45px}
.nav li.current{background:#1a1a1a;padding:0 16px}
.nav li:last-child{margin-left:auto;padding-right:26px}
.slider{left:130px;top:153px;width:941px;height:393px;background:#fff;padding:6px 5px;box-shadow:0 22px 22px -18px rgba(0,0,0,.25)}
.slide{width:100%;height:100%;background:linear-gradient(120deg,#c9b9aa 0%,#8a7d72 40%,#5d6b43 75%,#3f5530 100%)}
.dots{left:563px;top:504px;display:flex;gap:4px}
.dots i{width:15px;height:15px;border-radius:50%;background:#fff;display:block}
.dots i.on{background:#000}
.welcome-title{left:130px;top:588px;font-size:21px}
.welcome-text{left:131px;top:624px;width:930px;font-size:13px;line-height:23px}
.rule{height:1px;background:var(--rule)}
.what{left:130px;top:759px;width:300px;height:428px;background:var(--panel);border-radius:3px}
.what .heading{position:absolute;left:20px;top:18px;font-size:19px;color:#fff}
.what .photo{position:absolute;left:18px;top:57px;width:264px;height:162px;background:#fff;padding:5px}
.what .photo div{width:100%;height:100%;background:linear-gradient(135deg,#6b5a45,#a08f78 50%,#4e4a3d)}
.what p{position:absolute;left:17px;top:232px;width:270px;color:#ddd;font-size:13px;line-height:23px}
.btn{background:linear-gradient(var(--orange-light),var(--orange-dark));color:#fff;border-radius:2px;text-align:center}
.what .btn{position:absolute;left:17px;top:368px;width:115px;height:37px;line-height:37px;font-size:15px}
.gallery-title{left:475px;top:754px;font-size:21px}
.thumb{background:#fff;border:1px solid #ddd;padding:5px;box-shadow:0 1px 2px rgba(0,0,0,.06)}
.thumb div{width:100%;height:100%}
.news-title{left:475px;top:959px;font-size:21px}
.news-item{width:277px;height:180px}
.news-item .thumb{position:absolute;left:0;top:0;width:91px;height:78px}
.news-item h3{position:absolute;left:107px;top:-4px;width:175px;color:var(--orange-text);font-weight:400;font-size:15px;line-height:20px}
.news-item p{position:absolute;left:107px;top:38px;width:170px;font-size:13px;line-height:20px}
.news-item .date{position:absolute;right:-2px;top:151px;font-size:13px;color:#333;white-space:nowrap}
.news-item .date span{color:var(--orange-text)}
.footer{left:0;top:1210px;width:1200px;height:190px;background:var(--footer)}
.foot-brand{left:131px;top:1240px;width:68px;height:68px;display:flex;flex-direction:column;align-items:center;justify-content:center;gap:4px;font-weight:600;color:var(--orange-text);font-size:9px;text-align:center;line-height:1.1}
.foot-brand .mark{width:18px;height:18px;background:var(--orange-text)}
.copy{left:131px;top:1325px;font-size:13px;line-height:21px;color:#bbb}
.copy b{font-weight:400;color:#fff}
.foot-title{font-family:"Russo One",sans-serif;color:var(--orange-text);font-size:14px;letter-spacing:1px}
.email{left:530px;top:1267px;width:257px;height:33px;background:#666;color:#ccc;font-style:italic;font-size:13px;line-height:33px;padding-left:15px;border-radius:2px}
.signup{left:717px;top:1316px;width:70px;height:31px;line-height:31px;font-size:13px}
.social{left:866px;top:1267px;display:flex;gap:6px}
.social i{display:block;width:30px;height:30px;border-radius:3px}
</style>
</head>
<body>
<div class="page">
  <div class="abs top-band"></div>
  <div class="abs dark-band"></div>

  <div class="abs brand"><span class="mark"></span>BRIAR RIDGE<br>TARGET RANGE</div>

  <div class="abs call">
    <div class="label">Call Us Today:</div>
    <div class="phone">555 010 0199</div>
  </div>

  <ul class="abs nav">
    <li class="current">HOME</li>
    <li>ABOUT US</li>
    <li>SERVICES</li>
    <li>CLASSES</li>
    <li>MEMBERSHIP</li>
    <li>CALENDER</li>
    <li>CONTACT US</li>
  </ul>

  <div class="abs slider"><div class="slide" role="img" aria-label="Two shooters in ear protection aiming a rifle outdoors"></div></div>
  <div class="abs dots"><i class="on"></i><i></i><i></i><i></i></div>

  <h1 class="abs heading welcome-title">Welcome to <span>Briar Ridge</span></h1>
  <p class="abs welcome-text">Aliquam molestie, mi et imperdiet euismod, dui purus auctor tellus, et interdum lacus lectus et ante. Sed accumsan sollicitudin sapien, sit amet adipiscing turpis gravida ac. In congue, neque ac lobortis volutpat, libero mauris varius mi, vitae suscipit ipsum ligula vitae risus. Duis aliquam nibh a dui iaculis viverra id a velit. Vivamus egestas risus in magna varius commodo. Sed semper viverra egestas. Etiam pretium porttitor lectus, vel ornare neque porta volutpat.</p>
  <div class="abs rule" style="left:130px;top:736px;width:940px"></div>

  <section class="abs what">
    <h2 class="heading">What <span>We Do</span></h2>
    <div class="photo"><div role="img" aria-label="Young shooters with ear protection at a covered firing line"></div></div>
    <p>Aliquam molestie, mi et imperdiet euismod, dui purus auctor tellus, et interdum lacus lectus et ante. Sed accumsan sollicitudin sapien, sit amet adipiscing turpis gravida ac.</p>
    <div class="btn">Read More</div>
  </section>

  <h2 class="abs heading gallery-title">Our <span>Gallery</span></h2>
  <div class="abs thumb" style="left:475px;top:793px;width:192px;height:126px"><div role="img" aria-label="Instructor with students at an indoor range" style="background:linear-gradient(135deg,#6d6a66,#b3aaa0 55%,#8a4b3d)"></div></div>
  <div class="abs thumb" style="left:677px;top:793px;width:192px;height:126px"><div role="img" aria-label="Shooter aiming a rifle close up" style="background:linear-gradient(135deg,#1c1c1c,#4b4b4b 55%,#8a8fa0)"></div></div>
  <div class="abs thumb" style="left:879px;top:793px;width:192px;height:126px"><div role="img" aria-label="Shooter aiming a pistol at an indoor range" style="background:linear-gradient(135deg,#d8dce2,#a3a8ae 55%,#6d737a)"></div></div>
  <div class="abs rule" style="left:477px;top:946px;width:593px"></div>

  <h2 class="abs heading news-title">Latest <span>News</span></h2>
  <article class="abs news-item" style="left:475px;top:1002px">
    <div class="thumb"><div role="img" aria-label="Pistol shooter at indoor range" style="background:linear-gradient(135deg,#dfe3e8,#9aa2aa)"></div></div>
    <h3>Aliquam molestie, mi et imperdiet euismod...</h3>
    <p>In congue, neque ac lobortis volutpat, libero mauris varius mi, vitae suscipit ipsum ligula vitae risus....</p>
    <div class="date">Posted on <span>JAN 18, 2014</span></div>
  </article>
  <article class="abs news-item" style="left:794px;top:1002px">
    <div class="thumb"><div role="img" aria-label="Shotgun shooter outdoors" style="background:linear-gradient(135deg,#8fb6dc,#c9d9e6 55%,#6f6a52)"></div></div>
    <h3>Aliquam molestie, mi et imperdiet euismod...</h3>
    <p>In congue, neque ac lobortis volutpat, libero mauris varius mi, vitae suscipit ipsum ligula vitae risus....</p>
    <div class="date">Posted on <span>JAN 18, 2014</span></div>
  </article>

  <footer class="abs footer"></footer>
  <div class="abs foot-brand"><span class="mark"></span>BRIAR RIDGE<br>TARGET RANGE</div>
  <p class="abs copy">Copyright © 2014. <b>Briar Ridge</b>. All Right Reserved<br>Privacy Policy</p>

  <h4 class="abs foot-title" style="left:530px;top:1236px">Newsletter SignUp</h4>
  <div class="abs email">Enter Email</div>
  <div class="abs btn signup">SIGN UP</div>

  <h4 class="abs foot-title" style="left:864px;top:1236px">Connect Us</h4>
  <div class="abs social" aria-label="Social links">
    <i style="background:#3b5a98"></i>
    <i style="background:#4bb8e0"></i>
    <i style="background:#1f7bb6"></i>
    <i style="background:#f07b1a"></i>
    <i style="background:#c4302b"></i>
  </div>
</div>
</body>
</html>
```